依頼詳細
・余白のある、落ち着いたデザインを希望です。
・以下参考サイトのような色味(キーカラー)を希望です。
(デザインは極端に類似しないことが望ましい)
- https://rinpa-kissa.jp/
- https://hamonoya.com/
・サイトのメニューは
-ごあいさつ
-会社案内・沿革
-事業内容
-納入実績
-お問い合わせ
-みなせのものづくり(ブログ)
-ネットショップ
となる予定です。
この度は、「TOPページのデザイン」と、上記「下層ページのベースデザイン」を依頼いたします。
・レスポンシブでスマートフォンにも対応させます。
・TOPページにはNEWS(お知らせ)欄が入る予定です。
・最終的に当方でWordPressにて構築します。
・参考サイトのイメージにとらわれない自由なデザインでもOKです。
ぜひ様々なアイデアをご提案下さい。
サイトURL
ページ数
2ページ
希望イメージ
シンプル 複雑
単色 カラフル
暗い 明るい
日常 高級
遊び心 厳粛
未来的 伝統的
女性的 男性的
希望する色
茶系、背景は白でお願いいたします。
納品ファイル
• 高解像度JPG (.jpg)
• イラストレーター形式 (.ai)
• フォトショップ形式 (.psd)
• PNG形式 (.png)
補足説明
資料と素材写真を添付いたします。
写真は今後差し替え予定なのでダミーとしてお使いください。

素材画像で購入が必要なものがある場合、「Pexel Vault (https://vault.pexelmart.com/jp/)」より選定下さい。当方で購入しますので、ご提案の際はカンプ画像を利用いただき、採用後には素材のURL or ファイル番号をお伝えいただきます。

その他ご不明な点がございましたら、お気軽にご連絡下さい。

シンプルで飽きの来ないデザインをクライアント様が気に入りました。

この度は本当にたくさんのご提案をいただきましてまことにありがとうございました。
どのデザインも素敵で、選ぶのに時間がかかりまして申し訳ございませんでした。
またの機会がございましたらご提案ください。改めて御礼申し上げます。

```html
<!DOCTYPE html>
<html lang="ja">
<head>
<meta charset="UTF-8">
<title>角館　みなせ</title>
<link rel="stylesheet" href="https://fonts.googleapis.com/css2?family=Noto+Sans+JP:wght@400;700&display=swap">
<style>
  :root{
    --gold:#c8a545;
    --gold-soft:#d9c27c;
    --text:#b8953a;
    --bg:#ffffff;
    --footer:#c9a84a;
    --white:#ffffff;
  }
  *{margin:0;padding:0;box-sizing:border-box}
  html,body{width:1200px;height:4396px;overflow:hidden;background:var(--bg)}
  body{font-family:"Noto Sans JP",sans-serif;color:var(--text);position:relative}
  .social{position:absolute;top:26px;right:68px;display:flex;gap:12px}
  .social span{width:28px;height:28px;background:var(--gold);border-radius:4px;display:block}
  .site-title{position:absolute;top:196px;width:100%;text-align:center;font-size:62px;font-weight:700;color:var(--gold);letter-spacing:6px}
  .global-nav{position:absolute;top:396px;width:100%;display:flex;justify-content:center;gap:62px;font-size:17px;color:var(--gold-soft)}
  .hero{position:absolute;left:216px;top:560px;width:768px;height:480px;background:linear-gradient(160deg,#3a78c9 0%,#6ea3dd 45%,#2c3d5a 100%)}
  .tagline{position:absolute;top:1225px;width:100%;text-align:center;font-size:29px;color:var(--gold-soft);letter-spacing:2px}
  .section-title{position:absolute;width:100%;text-align:center;font-size:40px;font-weight:700;color:var(--gold)}
  .promise-title{top:1480px}
  .promise{position:absolute;left:130px;top:1620px;width:950px;height:500px;writing-mode:vertical-rl;font-size:22px;line-height:52px;letter-spacing:3px;color:var(--text)}
  .promise strong{color:#a8852f;font-size:23px}
  .news-title{top:2395px}
  .news{position:absolute;left:200px;top:2540px;width:800px;border-collapse:collapse;font-size:24px;color:var(--text)}
  .news td{border-bottom:2px solid var(--gold-soft);padding:14px 16px;vertical-align:top;line-height:34px}
  .news tr:first-child td{border-top:2px solid var(--gold-soft)}
  .news .date{width:300px}
  .news .who{width:150px}
  .access-title{top:3110px}
  .map{position:absolute;left:320px;top:3260px;width:590px;height:460px;background:linear-gradient(135deg,#eef0ec 0%,#e3e8df 60%,#d9e3ee 100%)}
  .address{position:absolute;left:320px;top:3765px;font-size:25px;line-height:36px;color:var(--text)}
  .footer{position:absolute;left:0;top:4056px;width:1200px;height:340px;background:var(--footer)}
  .footer-nav{position:absolute;top:150px;width:100%;display:flex;justify-content:center;gap:64px;font-size:17px;color:var(--white)}
</style>
</head>
<body>
  <div class="social" aria-label="SNS"><span></span><span></span><span></span></div>
  <h1 class="site-title">角館　みなせ</h1>
  <nav class="global-nav">
    <span>ごあいさつ</span><span>会社案内・沿革</span><span>事業内容</span><span>納品実績</span><span>お問い合わせ</span><span>ブログ</span><span>ネットショップ</span>
  </nav>
  <div class="hero" role="img" aria-label="祭りの衣装をまとった人形の写真、青空を背景に"></div>
  <p class="tagline">いつも変わらない品質の木型と型にはまらないお付き合いを。</p>

  <h2 class="section-title promise-title">お約束</h2>
  <div class="promise">
    <p><strong>あなたのえがいていることをかたちにします</strong></p>
    <p>角館みなせは、一般社団法人伝統工芸の店として創業以来、</p>
    <p>昔ながらの技法で木型をひとつひとつ手作りしてまいりま</p>
    <p>した。地元の職人が受け継いだ技術を大切にしながら、</p>
    <p>時代の求めに合わせた形づくりを続けております。</p>
    <p>菓子型や飾り型など、用途に応じた木型の製作のほか、</p>
    <p>お客様のご要望を丁寧にお聞きし、新しいかたちにも挑戦</p>
    <p>してまいります。素材選びから仕上げまで一貫して手がけ</p>
    <p>ることで、長く使える品質をお届けいたします。</p>
    <p>これからも、お客様の思いにそっと寄り添うものづくりを</p>
    <p>続けてまいります。</p>
  </div>

  <h2 class="section-title news-title">お知らせ</h2>
  <table class="news">
    <tr><td class="date">令和元年　十月三十一日</td><td class="who">角館　みなせ</td><td>HP新設いたしました。</td></tr>
    <tr><td class="date">令和元年　十一月一日</td><td class="who">角館　みなせ</td><td>HP新設いたしました。</td></tr>
    <tr><td class="date">令和元年十一月二十一日</td><td class="who">角館　みなせ</td><td>HP新設いたしました。</td></tr>
    <tr><td class="date">令和元年十一月二十一日</td><td class="who">角館　みなせ</td><td>HP新設いたしました。</td></tr>
  </table>

  <h2 class="section-title access-title">アクセス</h2>
  <div class="map" role="img" aria-label="店舗周辺の地図"></div>
  <address class="address" style="font-style:normal">
    〒014-0000<br>
    秋田県仙北市みなせ町北沢<br>
    12-3<br>
    TEL:0187-00-1234
  </address>

  <footer class="footer">
    <nav class="footer-nav">
      <span>ごあいさつ</span><span>会社案内・沿革</span><span>事業内容</span><span>納品実績</span><span>お問い合わせ</span><span>ブログ</span><span>ネットショップ</span>
    </nav>
  </footer>
</body>
</html>
```